Design some Business Cards for Brellor Motionworks

Brellor Motionworks, an automation design and services company specializing in packaging equipment in manufacturing facilities is in need of an updated business card design. I've got 3 different variations on the logo which I've attached. The primary hex colors are:

53D41D >> green
666666 >> grey

For the business cards, we'd like a 2-sided card. The info side should include:
- employee name
- title
- company name
- company address (6128 Foundry Lane, York, PA 17408)
- phone (both +1.717.555.0183 and 800.555.0147)
- e-mail

The web address [login to view URL] should appear somewhere on the card but I'll leave it up to you for the placement.

The color green should be highlighted on at least one side of the card. The logo cannot be altered in color or layout from the files provided.

PLEASE LIMIT YOUR SUBMISSIONS TO A MAXIMUM OF 12 DESIGNS.

I look forward to seeing the results.

Thanks in advance,
Mirabel

```html
<!DOCTYPE html>
<html lang="en">
<head>
<meta charset="utf-8">
<title>Brellor Motionworks Business Cards</title>
<link href="https://fonts.googleapis.com/css2?family=Roboto+Condensed:wght@400;500;700&display=swap" rel="stylesheet">
<style>
  :root {
    --green: #53d41d;
    --grey: #666666;
    --black: #0b0b0b;
    --white: #ffffff;
    --backdrop: #e7e7e4;
  }
  html, body {
    margin: 0;
    padding: 0;
    width: 1200px;
    height: 915px;
    overflow: hidden;
    background: var(--backdrop);
    font-family: "Roboto Condensed", Arial, sans-serif;
  }
  .canvas {
    position: relative;
    width: 1200px;
    height: 915px;
  }
  .card {
    position: absolute;
    top: 95px;
    width: 440px;
    height: 725px;
    border-radius: 24px;
    background: var(--black);
    overflow: hidden;
    box-shadow: 0 10px 30px rgba(0,0,0,0.25);
  }
  .card-back { left: 150px; }
  .card-front { left: 610px; }

  .brand-name {
    color: var(--green);
    font-weight: 500;
    letter-spacing: 1px;
    white-space: nowrap;
  }
  .card-back .brand {
    position: absolute;
    top: 340px;
    left: 0;
    width: 100%;
    text-align: center;
  }
  .card-back .brand-name { font-size: 34px; }

  .card-front .brand {
    position: absolute;
    top: 112px;
    left: 44px;
    display: flex;
    align-items: center;
    gap: 12px;
  }
  .brand-dot {
    width: 46px;
    height: 46px;
    border-radius: 50%;
    background: var(--grey);
    flex: none;
  }
  .card-front .brand-name { font-size: 34px; }

  .info-panel {
    position: absolute;
    left: 0;
    top: 0;
    width: 440px;
    height: 725px;
  }
  .person {
    position: absolute;
    right: 52px;
    top: 330px;
    text-align: right;
    color: var(--white);
  }
  .person-name {
    font-size: 23px;
    font-weight: 700;
    line-height: 1.1;
  }
  .person-title {
    font-size: 17px;
    font-weight: 400;
  }
  .contacts {
    position: absolute;
    right: 36px;
    top: 468px;
    margin: 0;
    padding: 0;
    list-style: none;
    color: var(--white);
    font-size: 16px;
    text-align: right;
  }
  .contacts li {
    display: flex;
    align-items: center;
    justify-content: flex-end;
    gap: 10px;
    height: 31px;
  }
  .contacts svg { width: 16px; height: 16px; fill: var(--white); flex: none; }
  .web-address {
    position: absolute;
    left: 0;
    bottom: 22px;
    width: 100%;
    text-align: center;
    color: var(--white);
    font-size: 20px;
  }
</style>
</head>
<body>
<main class="canvas">

  <section class="card card-back" aria-label="Card back">
    <div class="brand"><span class="brand-name">BRELLOR MOTIONWORKS</span></div>
  </section>

  <section class="card card-front" aria-label="Card front">
    <svg class="info-panel" viewBox="0 0 440 725" aria-hidden="true">
      <path d="M0 360 C 90 270, 250 240, 440 262 L440 640 L0 640 Z" fill="var(--green)"/>
    </svg>

    <div class="brand">
      <span class="brand-dot"></span>
      <span class="brand-name">BRELLOR</span>
    </div>

    <div class="person">
      <div class="person-name">EMPLOYEE NAME</div>
      <div class="person-title">Managing Director</div>
    </div>

    <ul class="contacts">
      <li>+1.717.555.0183
        <svg viewBox="0 0 24 24"><path d="M6.6 10.8a15 15 0 0 0 6.6 6.6l2.2-2.2a1 1 0 0 1 1-.25 11.4 11.4 0 0 0 3.6.57 1 1 0 0 1 1 1V20a1 1 0 0 1-1 1A17 17 0 0 1 3 4a1 1 0 0 1 1-1h3.5a1 1 0 0 1 1 1c0 1.25.2 2.45.57 3.57a1 1 0 0 1-.25 1z"/></svg>
      </li>
      <li>800.555.0147
        <svg viewBox="0 0 24 24"><path d="M7 1h10a2 2 0 0 1 2 2v18a2 2 0 0 1-2 2H7a2 2 0 0 1-2-2V3a2 2 0 0 1 2-2zm0 3v14h10V4zm5 15.5a1.2 1.2 0 1 0 0 2.4 1.2 1.2 0 0 0 0-2.4z"/></svg>
      </li>
      <li>mvance@brellormotion.com
        <svg viewBox="0 0 24 24"><path d="M2 5h20v14H2zm2 2v.4l8 5.1 8-5.1V7zm0 2.8V17h16V9.8l-8 5.1z"/></svg>
      </li>
      <li>6128 Foundry Lane, York, PA 17408
        <svg viewBox="0 0 24 24"><path d="M12 2a7 7 0 0 0-7 7c0 5 7 13 7 13s7-8 7-13a7 7 0 0 0-7-7zm0 9.5A2.5 2.5 0 1 1 12 6.5a2.5 2.5 0 0 1 0 5z"/></svg>
      </li>
    </ul>

    <div class="web-address">www.brellormotion.com</div>
  </section>

</main>
</body>
</html>
```